New Coworking Space in Zurich needs Grand Opening Invitation Card Design

Kestrawn is a new plug & play Coworking Space that offers startups and corporations flexible and inspiring office space together with leading-edge professional services. The space opens in April and we need an invitation card for our Grand Opening where we will invite corporate partners, our advisory board and startups. More detailed information about the space and the card as well as logo variations are attached.

Target Market(s)

The card will be sent to senior professionals, corporate partners, the advisory board and startups. Most work in the Technology / Marketing market and are interested in coworking.

Industry/Entity Type

Office

Font styles to use
Other font styles liked:
• Montserrat Light for text on back

Colors

Designer to choose colors to be used in the design.

Requirements
Must have
• a festive, modern look and feel to make the guests interested about our space and in joining the party. Front of the card needs to have the words 'Grand Opening' and 'Kestrawn'. More details and text are in the attached brief document.
Nice to have
• since we don’t have any pictures of the space yet, you could use symbols such as spotlights, a mirror ball or similar to illustrate a festive feeling or also write 'Grand Opening' in a special manner (for example in little spot lights, see an example attached in the brief). Give the feeling of collaboration, change, innovation and a nice fresh look.
Should not have
• The reason for the party is the opening of the coworking space, so it should not be in a gala/ball/luxurious manner and also needs to be professional, so not in a private birthday party look.

```html
<!DOCTYPE html>
<html lang="en">
<head>
<meta charset="utf-8">
<title>Kestrawn Grand Opening Invitation</title>
<link rel="stylesheet" href="https://fonts.googleapis.com/css2?family=Montserrat:ital,wght@0,400;0,600;0,700;1,400&family=Hind:wght@400;500;600&display=swap">
<style>
  :root {
    --paper: #ffffff;
    --frame: #3a3a3a;
    --night: #0b0b0b;
    --night-soft: #242424;
    --ink: #111111;
    --honey: #f6c726;
    --bulb: #ff9a1c;
    --bulb-glow: rgba(255, 140, 20, 0.75);
  }
  * { margin: 0; padding: 0; box-sizing: border-box; }
  html, body { width: 1200px; height: 1197px; overflow: hidden; background: var(--paper); }
  .sheet {
    position: relative; width: 1200px; height: 1197px;
    border: 2px solid var(--frame); background: var(--paper);
  }
  .card { position: absolute; top: 201px; width: 525px; height: 745px; overflow: hidden; }

  /* Front */
  .card-front { left: 75px; background: var(--night); }
  .front-backdrop {
    position: absolute; inset: 0;
    background: radial-gradient(ellipse at 35% 80%, var(--night-soft) 0%, var(--night) 70%);
  }
  .spotlight { position: absolute; inset: 0; }
  .headline {
    position: absolute; left: -40px; top: 232px; width: 600px;
    transform: rotate(-22deg); transform-origin: center;
    font-family: "Montserrat", sans-serif; font-weight: 700;
    font-size: 84px; line-height: 88px; letter-spacing: 5px;
    color: transparent; text-align: center;
    -webkit-text-stroke: 3px var(--bulb);
    text-shadow: 0 0 10px var(--bulb-glow), 0 0 22px rgba(255,120,0,0.4);
  }
  .headline span { display: block; }
  .headline .line-top { padding-left: 60px; }
  .front-brand {
    position: absolute; right: 18px; bottom: 26px; text-align: right;
  }
  .front-brand .brand-mark {
    display: inline-block; width: 26px; height: 26px; background: var(--honey);
    margin-right: 12px; vertical-align: middle;
  }
  .front-brand .brand-name {
    font-family: "Montserrat", sans-serif; font-weight: 700; font-size: 58px;
    line-height: 62px; color: var(--paper); vertical-align: middle;
  }
  .front-brand .brand-tag {
    font-family: "Montserrat", sans-serif; font-weight: 400; font-size: 27px;
    color: var(--paper); line-height: 32px;
  }

  /* Back */
  .card-back {
    left: 618px; background: var(--paper); border: 1.5px solid var(--frame);
    font-family: "Hind", sans-serif; color: var(--ink); text-align: center;
  }
  .back-brand { position: absolute; top: 16px; left: 0; right: 0; }
  .back-brand .brand-name {
    font-family: "Montserrat", sans-serif; font-weight: 700; font-size: 48px;
    line-height: 56px; color: var(--ink);
  }
  .back-brand .brand-tag {
    font-family: "Montserrat", sans-serif; font-size: 18px; line-height: 22px; color: var(--ink);
  }
  .mission { position: absolute; top: 118px; left: 20px; right: 20px; font-size: 14px; line-height: 18px; font-weight: 500; }
  .invite-label { position: absolute; top: 226px; left: 0; right: 0; font-size: 14px; font-weight: 600; letter-spacing: 0.3px; }
  .welcome { position: absolute; top: 316px; left: 0; right: 0; font-size: 14px; font-style: italic; font-weight: 500; }
  .event-details { position: absolute; top: 351px; left: 0; right: 0; font-size: 14px; line-height: 18px; font-weight: 500; }
  .rsvp { position: absolute; top: 460px; left: 0; right: 0; font-size: 14px; line-height: 18px; font-style: italic; font-weight: 500; }
  .signatory { position: absolute; font-family: "Montserrat", sans-serif; text-align: center; }
  .signatory .name { font-weight: 700; font-size: 12.5px; letter-spacing: 0.3px; }
  .signatory .role { font-style: italic; font-size: 10.5px; margin-top: 3px; }
  .sig-left { top: 604px; left: 50px; width: 180px; }
  .sig-right { top: 604px; left: 306px; width: 180px; }
  .sig-center { top: 648px; left: 178px; width: 180px; }
  .sig-center .role { margin-top: 0; }
</style>
</head>
<body>
<main class="sheet">
  <section class="card card-front" aria-label="Invitation front">
    <div class="front-backdrop" role="img" aria-label="Dark background with faint honeycomb pattern"></div>
    <svg class="spotlight" width="525" height="745" viewBox="0 0 525 745" aria-hidden="true">
      <defs>
        <linearGradient id="beam" x1="1" y1="0" x2="0.35" y2="0.55">
          <stop offset="0" stop-color="#f6c726" stop-opacity="0.75"/>
          <stop offset="1" stop-color="#f6c726" stop-opacity="0"/>
        </linearGradient>
        <filter id="soft"><feGaussianBlur stdDeviation="8"/></filter>
      </defs>
      <polygon points="525,0 525,55 400,330 250,290 470,0" fill="url(#beam)" filter="url(#soft)"/>
    </svg>
    <h1 class="headline"><span class="line-top">GRAND</span><span>OPENING</span></h1>
    <div class="front-brand">
      <div><span class="brand-mark"></span><span class="brand-name">Kestrawn</span></div>
      <div class="brand-tag">Coworking Ecosystem</div>
    </div>
  </section>

  <section class="card card-back" aria-label="Invitation back">
    <header class="back-brand">
      <div class="brand-name">Kestrawn</div>
      <div class="brand-tag">Coworking Ecosystem</div>
    </header>
    <p class="mission">We create innovation ecosystems in inspiring<br>and flexible workspaces in which startups, corporations and freelancers<br>can collaborate, exchange ideas and work on the future.</p>
    <p class="invite-label">PERSONAL INVITATION</p>
    <p class="welcome">We are thrilled to welcome you to our innovation ecosystem!</p>
    <p class="event-details">Thursday, 12 April 2018<br>6pm to open end<br>Lindenweg 48<br>8004 Zürich</p>
    <p class="rsvp">Join us to discover the possibilities within the ecosystem.<br>RSVP by 15 March 2018 at opening@kestrawn-cowork.ch<br>(leave space for signatures)</p>
    <div class="signatory sig-left"><div class="name">LUKAS BRENNER</div><div class="role">Co-Founder Kestrawn AG</div></div>
    <div class="signatory sig-right"><div class="name">MARCO FERRETTI</div><div class="role">Co-Founder Kestrawn AG</div></div>
    <div class="signatory sig-center"><div class="name">JONAS HALLBERG</div><div class="role">Co-Founder Kestrawn AG</div></div>
  </section>
</main>
</body>
</html>
```